Veterinary Hospital Brochure - 2 Drafts - 1 Normal and 1 Fun.

Meadowbrook Pet Hospital needs a brochure to promote our veterinary hospital. These will be delivered to local mailboxes. I would like to see atleast 2 submissions from each designer.
One submission conservative and A4 folded DL and another submission more radical and interesting with innovative folding or crazy concepts. Maybe the brochure could be designed to fold into a dog house ?
I want at least one version to be VERY SIMPLE AND INTIMATE.
Our existing website is here: http://furlane.example/ and our new website will look like this: http://trial4.pagemint.example/#home
Please use colors and images from the new website, and information from the old website. The heading font used in the new site is Qorvatype - Otter Tilt Sketchline
I want the brochure to be simple and engaging on first view, and then provide the opportunity to find more information if desired. The brochure needs to be captivating on the outside so people don't throw it away immediately.

We will soon need letterhead, flags, pens, business cards, signs and vouchers so there is the opportunity for more work for the successful designer.

Target Market(s)

Women 25 to 44

Industry/Entity Type

Veterinary

Contact Information for Business Card

Meadowbrook Pet Hospital
14 Marlow Crescent
Tamsworth Vale
NSW 2417
Phone: 02 61938205
Emergency: 0417360592
Fax: 02 83159462
www.meadowbrookvets.example
contact@meadowbrookvets.example

Font styles to use
Script

Requirements
Must have
• Colors from the new website: http://meadowbrookvets.example/ and new logo.
• Information from the old website: http://furlane.example/
• 2 drafts - A normal A4 folded DL flyer and an interesting crazy design.
Nice to have
• VERY SIMPLE
• Subdued
• Intimate
Should not have
• Intense colours
• Red

```html
<!DOCTYPE html>
<html lang="en">
<head>
<meta charset="utf-8">
<title>Meadowbrook Pet Hospital – Trifold Brochure</title>
<link rel="stylesheet" href="https://fonts.googleapis.com/css2?family=Bangers&family=Lato:wght@400;700&family=Oswald:wght@400;500&display=swap">
<style>
:root{
  --backdrop:#b3b3b3;
  --green:#6b9a37;
  --green-dark:#4f7d25;
  --orange:#f0862a;
  --brown:#4a2b16;
  --ink:#3b3b3b;
  --white:#ffffff;
}
*{box-sizing:border-box;margin:0;padding:0}
html,body{width:1200px;height:1200px;overflow:hidden;background:var(--backdrop)}
.canvas{width:1200px;height:1200px;position:relative;overflow:hidden;background:var(--backdrop)}
.stage{position:absolute;left:0;top:0;width:1400px;height:1400px;transform:scale(.857143);transform-origin:0 0}
.sheet{position:absolute;left:270px;width:859px;height:611px;overflow:hidden;background:var(--white);box-shadow:0 2px 6px rgba(0,0,0,.18)}
.sheet--outside{top:76px}
.sheet--inside{top:726px}
.sheet svg.art{position:absolute;left:0;top:0;width:859px;height:611px}
.fold{position:absolute;top:0;width:14px;height:611px;pointer-events:none}
.fold--a{left:286px;background:linear-gradient(90deg,rgba(0,0,0,0),rgba(0,0,0,.08),rgba(0,0,0,0))}
.fold--b{left:569px;background:linear-gradient(90deg,rgba(0,0,0,0),rgba(0,0,0,.10),rgba(0,0,0,0))}
.txt{position:absolute;font-family:'Lato',sans-serif;color:var(--ink)}
.body-copy{font-size:9.6px;line-height:14px}
.justify{text-align:justify}
.h-about{font-family:'Lato',sans-serif;font-size:21px;color:var(--orange);text-decoration:underline;text-underline-offset:3px}
.h-section{font-family:'Oswald',sans-serif;font-weight:400;font-size:14.5px;color:var(--orange)}
.h-sub{font-family:'Oswald',sans-serif;font-weight:400;font-size:13.5px;line-height:18px;color:var(--orange)}
.brand{position:absolute;text-align:center;font-family:'Oswald',sans-serif;font-weight:500;color:var(--brown);text-transform:uppercase;line-height:1.05}
.brand small{display:block;font-size:.55em;letter-spacing:.06em}
.welcome{position:absolute;left:596px;top:428px;width:263px;text-align:center;font-family:'Bangers',sans-serif;color:var(--orange);line-height:.95;text-shadow:1px 1px 0 var(--brown),-1px -1px 0 var(--brown),1px -1px 0 var(--brown),-1px 1px 0 var(--brown)}
.welcome .lead{display:block;font-size:27px;color:var(--white);letter-spacing:.02em}
.welcome .name{display:block;font-size:44px;letter-spacing:.01em}
.pill{position:absolute;height:24px;border-radius:12px;font-family:'Lato',sans-serif;font-weight:700;font-size:13px;letter-spacing:.12em;display:flex;align-items:center;justify-content:center}
.pill--dark{background:var(--brown);color:var(--white)}
.pill--orange{background:var(--orange);color:var(--brown)}
.contact{position:absolute;left:424px;top:466px;color:var(--white);font-family:'Lato',sans-serif}
.contact h3{font-size:13px;font-weight:700;text-decoration:underline;margin-bottom:10px}
.contact li{list-style:none;display:flex;align-items:center;gap:7px;font-size:10px;font-weight:700;height:16px}
.contact svg{width:10px;height:10px;flex:none}
.services{position:absolute;left:600px;top:30px;width:250px;color:var(--white);font-family:'Lato',sans-serif}
.services h4{font-size:10px;color:var(--orange);font-weight:700;margin-bottom:6px}
.services ul{display:grid;grid-template-columns:124px 124px;row-gap:1px}
.services li{list-style:none;font-size:10px;line-height:14px}
.services li::before{content:"•";color:var(--orange);margin-right:5px}
.badges{position:absolute;left:604px;top:130px;width:250px;display:grid;grid-template-columns:122px 122px;row-gap:14px;color:var(--white);font-family:'Lato',sans-serif;font-size:10px;line-height:14px}
.badge{display:flex;align-items:center;gap:8px}
.badge svg{width:28px;height:28px;flex:none}
</style>
</head>
<body>
<div class="canvas">
<div class="stage">

  <!-- Outside of brochure -->
  <section class="sheet sheet--outside">
    <svg class="art" viewBox="0 0 859 611" xmlns="http://www.w3.org/2000/svg">
      <defs>
        <linearGradient id="skyField" x1="0" y1="0" x2="0" y2="1">
          <stop offset="0" stop-color="#e9eef0"/><stop offset=".55" stop-color="#d9e2d2"/><stop offset=".72" stop-color="#9cbc55"/><stop offset="1" stop-color="#6f9a33"/>
        </linearGradient>
        <linearGradient id="dogHug" x1="0" y1="0" x2="1" y2="1">
          <stop offset="0" stop-color="#e6e8e2"/><stop offset=".45" stop-color="#c9a98a"/><stop offset=".7" stop-color="#5a4030"/><stop offset="1" stop-color="#a98462"/>
        </linearGradient>
        <linearGradient id="catLap" x1="0" y1="0" x2="1" y2="1">
          <stop offset="0" stop-color="#e8d9c4"/><stop offset=".5" stop-color="#b79a82"/><stop offset="1" stop-color="#7a6252"/>
        </linearGradient>
        <linearGradient id="puppy" x1="0" y1="0" x2="0" y2="1">
          <stop offset="0" stop-color="#ecd7b2"/><stop offset="1" stop-color="#d4b383"/>
        </linearGradient>
      </defs>
      <!-- panel 1 -->
      <rect x="0" y="0" width="293" height="611" fill="var(--green)"/>
      <path d="M38 230 C50 170 150 150 293 60 V448 C200 470 90 460 60 410 C30 360 28 290 38 230 Z" fill="var(--white)"/>
      <path d="M0 0 H242 C262 90 225 185 125 196 C70 200 30 188 0 168 Z" fill="url(#catLap)" role="img" aria-label="Photo of a woman reading with a tabby cat on her lap"/>
      <path d="M242 0 C262 90 225 185 125 196 C70 200 30 188 0 168" fill="none" stroke="var(--orange)" stroke-width="8"/>
      <path d="M34 330 C30 260 60 215 120 200" fill="none" stroke="var(--orange)" stroke-width="4"/>
      <path d="M0 448 C90 470 200 470 293 450 V611 H0 Z" fill="#8db25a" role="img" aria-label="Faded photo of a puppy giving a high five in the grass"/>
      <path d="M100 448 C170 470 240 462 293 452" fill="none" stroke="var(--orange)" stroke-width="4"/>
      <!-- panel 2 & 3 photo areas -->
      <rect x="293" y="0" width="283" height="440" fill="url(#skyField)" role="img" aria-label="Photo of an open green field under a soft sky"/>
      <rect x="576" y="0" width="283" height="440" fill="url(#dogHug)" role="img" aria-label="Photo of a woman hugging a shepherd dog"/>
      <!-- waves -->
      <path d="M293 426 C400 420 500 385 620 378 C720 374 800 380 859 400 V611 H293 Z" fill="var(--orange)"/>
      <path d="M293 440 C400 432 500 400 620 392 C720 388 800 398 859 420 V611 H293 Z" fill="var(--white)"/>
      <path d="M293 452 C400 444 500 414 620 406 C720 402 800 416 859 446 V611 H293 Z" fill="var(--green)"/>
      <!-- map circle -->
      <circle cx="428" cy="299" r="80" fill="#ebe9e3" role="img" aria-label="Street map showing the hospital location"/>
      <circle cx="428" cy="299" r="80" fill="none" stroke="var(--orange)" stroke-width="8"/>
      <!-- puppy -->
      <path d="M296 611 V470 C300 430 330 418 360 420 C395 422 412 450 418 490 L430 611 Z" fill="url(#puppy)" role="img" aria-label="Photo of a smiling golden retriever puppy"/>
    </svg>
    <div class="fold fold--a"></div><div class="fold fold--b"></div>

    <h2 class="txt h-about" style="left:80px;top:228px">About Us</h2>
    <p class="txt body-copy" style="left:68px;top:264px;width:198px">Meadowbrook Pet Hospital is a companion animal Veterinary Hospital In Tamsworth Vale. We heat Dogs. Cats, Reptiles, Rodents, Birds. and other little critters. As a companion animal only Hospital, we are dedicated to improving the wellbing of your beloved pets. We think they are part of the family and should receive absolute best possible care.</p>

    <div class="brand" style="left:353px;top:140px;width:150px;font-size:22px"><small>Meadowbrook Pet</small>Hospital</div>

    <div class="contact">
      <h3>Meadowbrook Pet Hospital</h3>
      <ul>
        <li><svg viewBox="0 0 10 10"><path d="M2 1 L4 1 L4.6 3 L3.4 4 C4 5.4 4.6 6 6 6.6 L7 5.4 L9 6 V8 C5 9 1 5 2 1Z" fill="#fff"/></svg>614829. 6148MPET</li>
        <li><svg viewBox="0 0 10 10"><rect x="1" y="4" width="8" height="4" rx="1" fill="#fff"/><rect x="3" y="1" width="4" height="3" fill="#fff"/></svg>61482075</li>
        <li><svg viewBox="0 0 10 10"><rect x="1" y="2.5" width="8" height="5.5" rx="1" fill="#fff"/><path d="M1.5 3 L5 6 L8.5 3" stroke="var(--green)" fill="none"/></svg>contact@furlane.example</li>
        <li><svg viewBox="0 0 10 10"><circle cx="5" cy="5" r="4" fill="none" stroke="#fff"/><path d="M1 5 H9 M5 1 C3 3 3 7 5 9 C7 7 7 3 5 1" stroke="#fff" fill="none" stroke-width=".8"/></svg>www.furlane.example</li>
        <li><svg viewBox="0 0 10 10"><circle cx="5" cy="5" r="4.5" fill="#fff"/></svg>Meadowbrook PetHospital</li>
      </ul>
    </div>

    <div class="brand" style="left:630px;top:94px;width:170px;font-size:30px"><small>Meadowbrook Pet</small>Hospital</div>

    <h1 class="welcome"><span class="lead">Welcome to</span><span class="name">Meadowbrook<br>Pet Hospital</span></h1>
    <div class="pill pill--dark" style="left:622px;top:567px;width:192px">www.furlane.example</div>
  </section>

  <!-- Inside of brochure -->
  <section class="sheet sheet--inside">
    <svg class="art" viewBox="0 0 859 611" xmlns="http://www.w3.org/2000/svg">
      <defs>
        <linearGradient id="grass" x1="0" y1="0" x2="0" y2="1">
          <stop offset="0" stop-color="#7fae3c"/><stop offset="1" stop-color="#4f7d25"/>
        </linearGradient>
        <linearGradient id="catKiss" x1="0" y1="0" x2="1" y2="0">
          <stop offset="0" stop-color="#9d8a74"/><stop offset=".5" stop-color="#d9b8a0"/><stop offset="1" stop-color="#5b3a28"/>
        </linearGradient>
        <linearGradient id="catRest" x1="0" y1="0" x2="1" y2="0">
          <stop offset="0" stop-color="#f2efe9"/><stop offset=".5" stop-color="#9a8b78"/><stop offset="1" stop-color="#e9e4dc"/>
        </linearGradient>
        <linearGradient id="vetDog" x1="0" y1="0" x2="1" y2="1">
          <stop offset="0" stop-color="#e8ece8"/><stop offset=".5" stop-color="#f1e6d8"/><stop offset="1" stop-color="#d5a762"/>
        </linearGradient>
      </defs>
      <!-- panel 3 background -->
      <path d="M560 0 H859 V611 H575 C600 520 600 400 560 320 C530 260 540 120 560 0 Z" fill="var(--green)"/>
      <path d="M560 0 C540 120 530 260 560 320 C600 400 600 520 575 611" fill="none" stroke="var(--orange)" stroke-width="14"/>
      <!-- photos -->
      <path d="M0 300 C100 285 220 290 293 310 V500 H0 Z" fill="url(#catKiss)" role="img" aria-label="Photo of a woman nuzzling a tabby cat"/>
      <path d="M0 290 C100 275 220 280 293 300" fill="none" stroke="var(--orange)" stroke-width="12"/>
      <path d="M293 320 C380 300 480 300 566 320 L586 520 H293 Z" fill="url(#catRest)" role="img" aria-label="Photo of a tabby cat resting"/>
      <path d="M0 500 C150 470 430 470 590 520 V611 H0 Z" fill="url(#grass)" role="img" aria-label="Photo of green grass"/>
      <path d="M0 505 C150 475 430 475 590 525" fill="none" stroke="var(--white)" stroke-width="8"/>
      <path d="M0 490 C150 462 430 462 590 512" fill="none" stroke="var(--orange)" stroke-width="10"/>
      <path d="M690 250 C700 210 760 200 800 220 C830 235 840 290 830 360 H690 Z" fill="#b6a48c" role="img" aria-label="Photo of a tabby kitten"/>
      <path d="M585 400 C640 380 720 380 859 400 V611 H585 Z" fill="url(#vetDog)" role="img" aria-label="Photo of a vet with a golden retriever and kittens"/>
      <path d="M585 400 C640 380 720 380 859 400" fill="none" stroke="var(--orange)" stroke-width="10"/>
      <circle cx="612" cy="364" r="84" fill="#8a6a4c" role="img" aria-label="Photo of the hospital reception area"/>
      <circle cx="612" cy="364" r="84" fill="none" stroke="var(--orange)" stroke-width="8"/>
    </svg>
    <div class="fold fold--a"></div><div class="fold fold--b"></div>

    <h2 class="txt h-section" style="left:38px;top:30px">About Us</h2>
    <p class="txt body-copy justify" style="left:38px;top:56px;width:212px">Complimentary Nail Clippin Meadowbrook Pet Hospital provides nail clipping. All we ask is a note donation to Guide Paws Trust.</p>
    <p class="txt body-copy" style="left:38px;top:122px;width:212px">Meadowbrook Pet Hospital Is built on the grounds of a chapel built in 1897. The chapel hall has been converted into a beautiful reception area</p>
    <p class="txt body-copy justify" style="left:38px;top:169px;width:212px">We have constructed a modem veterinary hospital with small animal surgical facilities, X-ray. ultrasound, dog and cat wards. laboratory, isolation, multiple consultation rooms and a huge treatment area. Come in for a tour of our facility or go www.furlane.example</p>
    <div class="pill pill--orange" style="left:58px;top:566px;width:192px">www.furlane.example</div>

    <h2 class="txt h-section" style="left:316px;top:30px">Puppy Classes</h2>
    <p class="txt body-copy" style="left:316px;top:56px;width:186px;line-height:12px">Meadowbrook Pet Hospital runs a 5 week puppy class. These are great fun and provide ssential socialisation and training for you and your puppy<br>The classes prevent a range of behavioural issues and are an essential port of our prevention is better than cure philosophy.</p>
    <p class="txt h-sub" style="left:316px;top:178px;width:210px">Do all of these and you will keep us pets healthy and happy.</p>
    <p class="txt body-copy" style="left:316px;top:229px;width:210px">Meadowbrook Pet Hospital provides gold standard pet health care. This means we offer you the best possible care and remind you when it is due.</p>
    <div class="brand" style="left:316px;top:338px;width:102px;font-size:17px"><small>Meadowbrook Pet</small>Hospital</div>
    <div class="pill pill--orange" style="left:348px;top:566px;width:190px">www.furlane.example</div>

    <div class="services">
      <h4>This includes:</h4>
      <ul>
        <li>Vaccination</li><li>Microchipping</li>
        <li>Desexing</li><li>Intestinal Worming</li>
        <li>Hearlworm Prevention</li><li>Dental Care</li>
        <li>Flea Prevention</li><li>Premium Food</li>
      </ul>
    </div>
    <div class="badges">
      <div class="badge"><svg viewBox="0 0 28 28"><rect x="6" y="3" width="14" height="19" rx="2" fill="#fff"/><circle cx="18" cy="20" r="6" fill="#fff" stroke="var(--green)" stroke-width="1.5"/></svg>Registered<br>Veterinarians</div>
      <div class="badge"><svg viewBox="0 0 28 28"><rect x="3" y="5" width="20" height="14" rx="1" fill="none" stroke="#fff" stroke-width="2"/><path d="M9 23 H17 M13 19 V23" stroke="#fff" stroke-width="2"/></svg>Pre-Export<br>Testing</div>
      <div class="badge"><svg viewBox="0 0 28 28"><circle cx="14" cy="14" r="12" fill="none" stroke="#fff" stroke-width="2"/><path d="M14 7 V21 M7 14 H21" stroke="#fff" stroke-width="4"/></svg>Registered<br>Hospital</div>
      <div class="badge"><svg viewBox="0 0 28 28"><rect x="4" y="3" width="20" height="22" rx="2" fill="none" stroke="#fff" stroke-width="2"/><rect x="9" y="8" width="10" height="10" fill="#fff"/></svg>Compliant<br>Radiology</div>
    </div>
  </section>

</div>
</div>
</body>
</html>
```